LORM Business Card Design Project

Company Name: LORM (Bright Harbor Computing Solutions) PGH.
Office Address: Office No 718, Saffron Crest Tower, Palmwood Garden Heights, Dubai, U.A.E
Company line of business:
1) Currently we have a POS solution for retail outlets like duty free shops, supermarkets, department stores etc... The solution is deployed in Coastline Travel Retail on 350 POS and in Sandgate Airport Retail on 100 POS. So our main line of business is the deployment of this solution in retail outlets locally or regionally. We have already deployed the solution in India and Australia.
2) Integration of other third party POS systems with an online credit authorization netwotk in the UAE. This will enable POS applications to connect directly to the acquiring banks without needing an EFT terminal like Paxtrel or Movarski. The credit card payment is completed at the POS.
3) Other solutions that are targeting retail outlets like mobile POS, queue busting solutions, stock taking solutions using hand held devices, transaction capture systems, etc...
4) Other IT services like support of call center solutions from Northwind Callworks and development of new solutions as per customer requirements.
We need a business card design for the company. We don't have any specific requirements and will eave up to the designers to come up with creative designs. At the moment we still don't have a letter head design and the only thing that we have is the company logo that we will upload shortly.
Updates
Dear All,
I just uploaded the logo source files. I am sorry for the delay.
Regards
Samir Odwani
I would like the business cards to have the following details:
Company Tel No
Company Fax No
Company Website Address
Employee Name
Employee Title
Employee Mobile Number
Employee Email Address

```html
<!DOCTYPE html>
<html lang="en">
<head>
<meta charset="utf-8">
<title>LORM Business Card</title>
<link rel="stylesheet" href="https://fonts.googleapis.com/css2?family=Questrial&family=Poppins:wght@600&display=swap">
<style>
  :root {
    --backdrop: #e6e6e6;
    --card: #ffffff;
    --ink: #111111;
    --icon-blue: #1f8fd6;
    --mark-blue: #1b74c4;
    --band: #000000;
    --band-text: #ffffff;
  }
  * { margin: 0; padding: 0; box-sizing: border-box; }
  html, body {
    width: 1200px; height: 900px; overflow: hidden;
    background: var(--backdrop);
    font-family: "Questrial", sans-serif;
    color: var(--ink);
  }
  .canvas { position: relative; width: 1200px; height: 900px; }

  .card {
    position: absolute;
    background: var(--card);
    border-radius: 18px;
    overflow: hidden;
    box-shadow: 0 2px 6px rgba(0,0,0,0.12);
  }
  .card-front { left: 110px; top: 40px; width: 660px; height: 400px; }
  .card-back  { left: 430px; top: 470px; width: 670px; height: 390px; }

  .brand { position: absolute; display: flex; align-items: center; }
  .brand-dot { border-radius: 50%; background: var(--mark-blue); flex: none; }
  .brand-name {
    font-family: "Questrial", sans-serif;
    color: var(--ink);
    letter-spacing: 0.02em;
    line-height: 1;
  }
  .card-front .brand { left: 90px; top: 140px; }
  .card-front .brand-dot { width: 110px; height: 110px; margin-right: 34px; }
  .card-front .brand-name { font-size: 118px; }

  .card-back .brand { left: 38px; top: 110px; }
  .card-back .brand-dot { width: 62px; height: 62px; margin-right: 18px; }
  .card-back .brand-name { font-size: 66px; }

  .contact { position: absolute; left: 370px; top: 70px; }
  .person-name { font-family: "Poppins", sans-serif; font-weight: 600; font-size: 16px; line-height: 1.1; }
  .person-title { font-family: "Poppins", sans-serif; font-weight: 600; font-size: 14px; line-height: 1.1; margin-bottom: 14px; }
  .contact-list { list-style: none; }
  .contact-item { display: flex; align-items: center; height: 27px; font-size: 13px; }
  .contact-icon { width: 18px; height: 18px; margin-right: 18px; fill: var(--icon-blue); flex: none; }

  .web-band {
    position: absolute; left: 0; right: 0; bottom: 26px; height: 50px;
    background: var(--band); color: var(--band-text);
    display: flex; align-items: center; justify-content: center;
    font-size: 19px; letter-spacing: 0.55em;
  }
</style>
</head>
<body>
<main class="canvas">

  <section class="card card-front" aria-label="Business card front">
    <div class="brand">
      <span class="brand-dot"></span>
      <span class="brand-name">LORM</span>
    </div>
  </section>

  <section class="card card-back" aria-label="Business card back">
    <div class="brand">
      <span class="brand-dot"></span>
      <span class="brand-name">LORM</span>
    </div>

    <div class="contact">
      <p class="person-name">Daniel Reyes</p>
      <p class="person-title">Director</p>
      <ul class="contact-list">
        <li class="contact-item">
          <svg class="contact-icon" viewBox="0 0 24 24" aria-label="Telephone"><path d="M3 8c0-3 4-5 9-5s9 2 9 5v2h-5V8c-1-1-7-1-8 0v2H3zM6 12h12l2 9H4z"/><circle cx="12" cy="16" r="2.4" fill="#fff"/></svg>
          <span>xxx-xxxxx</span>
        </li>
        <li class="contact-item">
          <svg class="contact-icon" viewBox="0 0 24 24" aria-label="Fax"><path d="M6 2h10l2 2v5H6zM3 10h18v9H3zM7 15h10v7H7z"/></svg>
          <span>xxx-xxxxx</span>
        </li>
        <li class="contact-item">
          <svg class="contact-icon" viewBox="0 0 24 24" aria-label="Website"><path d="M12 2a10 10 0 1 0 0 20 10 10 0 0 0 0-20zm0 2c1.5 1.8 2.4 4.8 2.5 7h-5C9.6 8.8 10.5 5.8 12 4zM4.1 13h3.4c.1 2 .6 4 1.5 5.6A8 8 0 0 1 4.1 13zm0-2A8 8 0 0 1 9 5.4C8.1 7 7.6 9 7.5 11zM12 20c-1.5-1.8-2.4-4.8-2.5-7h5c-.1 2.2-1 5.2-2.5 7zm3-1.4c.9-1.6 1.4-3.6 1.5-5.6h3.4a8 8 0 0 1-4.9 5.6zM16.5 11c-.1-2-.6-4-1.5-5.6a8 8 0 0 1 4.9 5.6z"/></svg>
          <span>www.lorm-pgh.com</span>
        </li>
        <li class="contact-item">
          <svg class="contact-icon" viewBox="0 0 24 24" aria-label="Mobile"><path d="M8 1h2v3h5a2 2 0 0 1 2 2v15a2 2 0 0 1-2 2H9a2 2 0 0 1-2-2V6a2 2 0 0 1 1-1.7z"/><rect x="9.5" y="7" width="5" height="5" fill="#fff"/></svg>
          <span>xxx-xxxxx</span>
        </li>
        <li class="contact-item">
          <svg class="contact-icon" viewBox="0 0 24 24" aria-label="Email"><path d="M2 5h20v14H2z"/><path d="M2 5l10 8 10-8" fill="none" stroke="#fff" stroke-width="1.6"/></svg>
          <span>myemail@lorm-pgh.com</span>
        </li>
      </ul>
    </div>

    <div class="web-band">www.lorm-pgh.com</div>
  </section>

</main>
</body>
</html>
```